Website re-design for Brookvane LLC website ( has existing website )

Looking to do a complete re-design of Brookvanellc. The existing website is dated and built in wordpress. The new website will not be wordpress. The project folder includes an overview.txt file with details on the project. The file also contains a list of websites that he/she likes which I am sure is very helpful .
Number of Pages Required
1 page

```html
<!DOCTYPE html>
<html lang="en">
<head>
<meta charset="utf-8">
<title>Brookvane LLC</title>
<link href="https://fonts.googleapis.com/css2?family=Montserrat:wght@300;400;500;600;700;800&family=Open+Sans:ital,wght@0,400;0,600;1,400&display=swap" rel="stylesheet">
<style>
:root{
  --blue:#1e88e5;
  --blue-dark:#1565c0;
  --ink:#1d2733;
  --text:#55606c;
  --soft:#eef2f6;
  --white:#ffffff;
  --orange:#f57c00;
  --photo-lake:#4f81a8;
  --photo-lake-deep:#2f5f84;
}
*{box-sizing:border-box;margin:0;padding:0}
html,body{width:1200px;height:4068px;overflow:hidden}
body{position:relative;background:var(--white);font-family:"Open Sans",sans-serif;color:var(--text)}
.abs{position:absolute}
h1,h2,h3,.heading{font-family:"Montserrat",sans-serif;color:var(--ink)}

/* header */
.site-header{position:absolute;top:0;left:0;width:1200px;height:72px;background:var(--white);z-index:5;display:flex;align-items:center;padding:0 40px;box-shadow:0 2px 10px rgba(0,0,0,.08)}
.brand{display:flex;align-items:center;gap:10px}
.brand-dot{width:34px;height:34px;border-radius:50%;background:var(--blue)}
.brand-name{font-family:"Montserrat",sans-serif;font-weight:700;font-size:24px;color:var(--blue-dark)}
.main-nav{margin-left:auto;display:flex;align-items:center;gap:30px;font-family:"Montserrat",sans-serif;font-size:15px;font-weight:500;color:var(--ink)}
.main-nav .active{color:var(--blue);border-bottom:2px solid var(--blue);padding-bottom:4px}
.main-nav .pill{border:2px solid var(--blue);color:var(--blue);border-radius:22px;padding:8px 22px}

/* hero */
.hero{position:absolute;top:0;left:0;width:1200px;height:800px;overflow:hidden}
.hero-photo{position:absolute;inset:0;background:linear-gradient(180deg,var(--photo-lake) 0%,var(--photo-lake-deep) 100%)}
.hero-title{position:absolute;top:256px;left:0;width:1200px;text-align:center;color:var(--white);font-family:"Montserrat",sans-serif;text-shadow:0 2px 8px rgba(0,0,0,.3)}
.hero-title .light{font-weight:400;font-size:46px;letter-spacing:2px;display:block;line-height:1.15}
.hero-title .bold{font-weight:700;font-size:50px;letter-spacing:1px;display:block;line-height:1.15;margin-top:2px}
.btn-solid{display:inline-block;background:var(--blue);color:var(--white);font-family:"Montserrat",sans-serif;font-weight:700;font-size:14px;padding:16px 34px;border-radius:3px}
.hero-cta{position:absolute;top:396px;left:530px}
.hero-arrow{position:absolute;top:330px}

/* about */
.about-photo-ring{position:absolute;top:800px;left:116px;width:450px;height:450px;border-radius:50%;border:4px solid var(--blue);padding:10px;background:var(--white)}
.about-photo{width:100%;height:100%;border-radius:50%;background:linear-gradient(180deg,#7fa9c9 0%,#557f9f 100%)}
.about-text{position:absolute;top:848px;left:640px;width:470px}
.eyebrow{font-family:"Montserrat",sans-serif;color:var(--blue);font-size:16px;font-weight:500;letter-spacing:1px}
.about-text h2{font-size:34px;font-weight:800;line-height:1.2;margin:6px 0 18px}
.about-text p{font-size:15px;line-height:1.65}
.btn-outline{display:inline-block;border:2px solid var(--blue);color:var(--blue-dark);font-family:"Montserrat",sans-serif;font-weight:600;font-size:13px;padding:12px 28px;border-radius:3px}
.about-text .btn-outline{margin-top:28px}

/* services */
.services-band{position:absolute;top:1300px;left:0;width:1200px;height:700px}
.services-head{position:absolute;top:1362px;left:0;width:1200px;text-align:center}
.services-head h2{font-size:32px;font-weight:700;margin-top:4px}
.service-card{position:absolute;top:1480px;width:230px;height:360px;background:var(--white);border-radius:16px;box-shadow:0 6px 18px rgba(13,42,74,.1);text-align:center;padding-top:20px}
.service-photo{width:186px;height:186px;border-radius:50%;margin:0 auto;border:4px solid var(--blue);padding:6px;background:var(--white)}
.service-photo div{width:100%;height:100%;border-radius:50%}
.service-card h3{font-size:14px;font-weight:700;margin:18px 12px 8px;line-height:1.35}
.service-card p{font-size:11px;line-height:1.5;margin:0 26px;color:#8a939c}
.card-chevron{position:absolute;bottom:-2px;left:99px;width:32px;height:32px;border-radius:50%;background:var(--blue)}
.services-cta{position:absolute;top:1876px;left:468px;padding:16px 44px}

/* gallery */
.gallery-head{position:absolute;top:2062px;left:0;width:1200px;text-align:center;font-size:32px;font-weight:700}
.before-after{position:absolute;top:2164px;width:492px;height:318px;display:flex;overflow:hidden}
.before-after div{flex:1}
.slider-knob{position:absolute;top:2302px;width:40px;height:40px;border-radius:50%;background:rgba(255,255,255,.85);border:2px solid var(--white)}

/* testimonials */
.testimonials{position:absolute;top:2560px;left:0;width:1200px;height:520px;background:linear-gradient(180deg,#e4edf3 0%,#dfe6e2 100%)}
.testimonials-head{position:absolute;top:2620px;left:0;width:1200px;text-align:center;font-size:32px;font-weight:700;z-index:1}
.quote-card{position:absolute;top:2746px;left:282px;width:636px;height:244px;background:var(--white);border-radius:6px;border-bottom:4px solid var(--blue);box-shadow:0 8px 24px rgba(13,42,74,.15);text-align:center;padding:54px 60px 0;z-index:1}
.quote-badge{position:absolute;top:-28px;left:290px;width:56px;height:56px;border-radius:50%;background:var(--blue);display:flex;align-items:center;justify-content:center}
.quote-card blockquote{font-style:italic;font-size:16px;line-height:1.6;color:var(--ink)}
.quote-card .who{margin-top:16px;font-family:"Montserrat",sans-serif;font-weight:700;font-size:14px;color:var(--ink)}
.quote-card .where{font-size:13px;font-style:italic}
.t-arrow{position:absolute;top:2840px;z-index:1}

/* contact */
.contact{position:absolute;top:3060px;left:0;width:1200px;height:700px}
.contact-head{position:absolute;top:3150px;left:176px;color:var(--white);font-size:34px;font-weight:700}
.contact-head::after{content:"";display:block;width:54px;height:3px;background:var(--white);margin-top:6px}
.field{position:absolute;left:176px;width:420px;height:46px;background:var(--white);display:flex;align-items:center;gap:12px;padding:0 16px;font-size:14px;color:#6b747c}
.field.message{height:96px;align-items:flex-start;padding-top:14px}
.send-btn{position:absolute;top:3498px;left:176px;background:var(--orange);color:var(--white);font-family:"Montserrat",sans-serif;font-weight:700;font-size:14px;padding:16px 30px;border-radius:24px}
.contact-photo-ring{position:absolute;top:3120px;left:650px;width:456px;height:456px;border-radius:50%;border:8px solid var(--white)}
.contact-photo{width:100%;height:100%;border-radius:50%;background:linear-gradient(180deg,#9fb7c9 0%,#6f96b8 100%)}

/* footer */
.footer-brand{position:absolute;top:3738px;left:120px;width:250px}
.footer-brand .brand-dot{width:40px;height:40px}
.footer-brand .brand-name{font-size:26px}
.footer-brand p{font-size:12px;line-height:1.6;margin-top:18px}
.socials{display:flex;gap:10px;margin-top:18px}
.socials span{width:30px;height:30px;border-radius:50%;background:var(--blue)}
.footer-col{position:absolute;top:3744px}
.footer-col h4{font-family:"Montserrat",sans-serif;font-size:17px;font-weight:700;color:var(--ink);border-left:4px solid var(--blue);padding-left:10px;margin-bottom:18px}
.link-grid{display:grid;grid-template-columns:140px 140px;row-gap:14px;font-size:14px;padding-left:14px}
.contact-list{list-style:none;font-size:14px;padding-left:14px}
.contact-list li{display:flex;align-items:flex-start;gap:12px;margin-bottom:16px;line-height:1.4}
.copyright{position:absolute;top:4032px;left:0;width:1200px;height:36px;border-top:1px solid #e2e7ec;text-align:center;font-size:12px;line-height:36px}
</style>
</head>
<body>

<section class="hero">
  <div class="hero-photo" role="img" aria-label="Wooded lake shore with pine trees reflected in calm water"></div>
  <h1 class="hero-title"><span class="light">WE KNOW THERE IS</span><span class="bold">NO LIFE LIKE THE LAKE LIFE</span></h1>
  <a class="btn-solid hero-cta">FREE ESTIMATE</a>
  <svg class="hero-arrow" style="left:22px" width="24" height="50" viewBox="0 0 24 50"><path d="M20 4 4 25l16 21" fill="none" stroke="#fff" stroke-width="4"/></svg>
  <svg class="hero-arrow" style="left:1154px" width="24" height="50" viewBox="0 0 24 50"><path d="M4 4l16 21L4 46" fill="none" stroke="#fff" stroke-width="4"/></svg>
  <svg class="abs" style="left:0;top:600px" width="1200" height="200" viewBox="0 0 1200 200" preserveAspectRatio="none">
    <path d="M0 200V150C300 200 800 200 1200 40V200Z" fill="#fff"/>
    <path d="M0 150C300 200 800 200 1200 40" fill="none" stroke="#1e88e5" stroke-width="8"/>
  </svg>
</section>

<header class="site-header">
  <div class="brand"><span class="brand-dot"></span><span class="brand-name">Brookvane</span></div>
  <nav class="main-nav">
    <span class="active">Services</span><span>About Us</span><span>FAQs</span><span>Employment</span><span>Testimonials</span><span>Gallery</span><span class="pill">Contact Us</span>
  </nav>
</header>

<section class="about">
  <div class="about-photo-ring"><div class="about-photo" role="img" aria-label="Bow of a canoe on a calm lake facing a pine covered island"></div></div>
  <div class="about-text">
    <div class="eyebrow">ABOUT US</div>
    <h2>AQUATIC INNOVATORS,<br>AT YOUR SERVICE.</h2>
    <p>Brookvane LLC is a company formed in response to the increasing incidence of invasive species in Minnesota's lakes and water systems. The impact of these fast growing nuisances inspired our venture to effectively control unwanted lake weeds. Brookvane LLC helps provide the enjoyable weed-free lake environment craved by water enthusiasts.</p>
    <a class="btn-outline">LEARN MORE</a>
  </div>
</section>

<section class="services">
  <svg class="services-band" viewBox="0 0 1200 700" preserveAspectRatio="none">
    <path d="M0 60C400 0 800 0 1200 60V620C800 700 400 700 0 620Z" fill="#eef2f6"/>
    <path d="M0 620C400 700 800 700 1200 620" fill="none" stroke="#1e88e5" stroke-width="6"/>
  </svg>
  <div class="services-head"><div class="eyebrow">WHAT WE DO</div><h2>DOCK INSTALL AND REMOVAL SERVICES</h2></div>

  <article class="service-card" style="left:102px">
    <div class="service-photo"><div role="img" aria-label="Quiet lake view framed by trees" style="background:linear-gradient(180deg,#7ea6c4,#5c86a6)"></div></div>
    <h3>ZEBRA MUSSEL<br>REMOVAL</h3><p>Careful clearing of shells from docks and lifts.</p>
    <span class="card-chevron"><svg width="32" height="32" viewBox="0 0 32 32"><path d="M10 13l6 6 6-6" fill="none" stroke="#fff" stroke-width="3"/></svg></span>
  </article>
  <article class="service-card" style="left:358px">
    <div class="service-photo"><div role="img" aria-label="Boat lift canopy over the water" style="background:linear-gradient(180deg,#d2dde6,#b3c7d6)"></div></div>
    <h3>CANOPY SERVICES</h3><p>Canopy covers fitted, repaired and stored each year.</p>
    <span class="card-chevron"><svg width="32" height="32" viewBox="0 0 32 32"><path d="M10 13l6 6 6-6" fill="none" stroke="#fff" stroke-width="3"/></svg></span>
  </article>
  <article class="service-card" style="left:614px">
    <div class="service-photo"><div role="img" aria-label="Work barge loaded with dock sections" style="background:linear-gradient(180deg,#9a8a88,#7c7a80)"></div></div>
    <h3>BARGE SERVICES<br>(FALL 2022)</h3><p>Heavy loads moved safely across your lake.</p>
    <span class="card-chevron"><svg width="32" height="32" viewBox="0 0 32 32"><path d="M10 13l6 6 6-6" fill="none" stroke="#fff" stroke-width="3"/></svg></span>
  </article>
  <article class="service-card" style="left:870px">
    <div class="service-photo"><div role="img" aria-label="Dock with boat lift on a sunny lake" style="background:linear-gradient(180deg,#86adc9,#5d8aad)"></div></div>
    <h3>DOCK LIFT SERVICES<br>(FALL 2022)</h3><p>Lifts set in spring and pulled before ice.</p>
    <span class="card-chevron"><svg width="32" height="32" viewBox="0 0 32 32"><path d="M10 13l6 6 6-6" fill="none" stroke="#fff" stroke-width="3"/></svg></span>
  </article>

  <a class="btn-outline services-cta">VIEW ALL SERVICES</a>
</section>

<section class="gallery">
  <h2 class="gallery-head">BEFORE &amp; AFTER GALLERY</h2>
  <div class="before-after" style="left:100px" role="img" aria-label="Weedy dock shoreline before clearing beside the same dock after clearing">
    <div style="background:#7d8f72"></div>
    <div style="background:#98a3a6"></div>
  </div>
  <div class="before-after" style="left:608px" role="img" aria-label="Shallow lake bottom overgrown with weeds before and clear after">
    <div style="background:#8c8560"></div>
    <div style="background:#66704c"></div>
  </div>
  <span class="slider-knob" style="left:326px"></span>
  <span class="slider-knob" style="left:834px"></span>
</section>

<section>
  <div class="testimonials" role="img" aria-label="Faded view of a forest lake behind the testimonials"></div>
  <h2 class="testimonials-head">TESTIMONIALS</h2>
  <svg class="t-arrow" style="left:206px" width="20" height="40" viewBox="0 0 20 40"><path d="M16 4 4 20l12 16" fill="none" stroke="#1d2733" stroke-width="3"/></svg>
  <svg class="t-arrow" style="left:974px" width="20" height="40" viewBox="0 0 20 40"><path d="M4 4l12 16L4 36" fill="none" stroke="#1d2733" stroke-width="3"/></svg>
  <div class="quote-card">
    <span class="quote-badge"><svg width="26" height="20" viewBox="0 0 26 20"><path d="M0 20V10Q0 2 9 0v4Q5 5 5 10h5v10ZM15 20V10q0-8 9-10v4q-4 1-4 6h5v10Z" fill="#fff"/></svg></span>
    <blockquote>Everyone used to jump off the water trampoline and instantly get tangled in lake weeds. We contacted Brookvane and their SCUBA divers have now been solving our problem for the past 4 years!</blockquote>
    <div class="who">Pine Hollow Shore Association</div>
    <div class="where">(Lake Alder)</div>
  </div>
</section>

<section>
  <svg class="contact" viewBox="0 0 1200 700" preserveAspectRatio="none">
    <defs><linearGradient id="contactFill" x1="0" y1="0" x2="0" y2="1"><stop offset="0" stop-color="#1f8fe8"/><stop offset="1" stop-color="#1e7fd6"/></linearGradient></defs>
    <path d="M0 0H1200V560C800 700 400 700 0 600Z" fill="url(#contactFill)"/>
  </svg>
  <h2 class="contact-head">CONTACT US</h2>
  <div class="field" style="top:3224px"><svg width="16" height="16" viewBox="0 0 16 16"><circle cx="8" cy="5" r="3.5" fill="#1e88e5"/><path d="M1 16c0-4 3-6 7-6s7 2 7 6Z" fill="#1e88e5"/></svg>Your Name</div>
  <div class="field" style="top:3282px"><svg width="16" height="16" viewBox="0 0 16 16"><path d="M3 1l3 3-2 2q2 4 6 6l2-2 3 3-2 2Q5 15 1 3Z" fill="#1e88e5"/></svg>Phone number</div>
  <div class="field" style="top:3340px"><svg width="16" height="16" viewBox="0 0 16 16"><rect x="1" y="3" width="14" height="10" fill="none" stroke="#1e88e5" stroke-width="1.6"/><path d="M1 3l7 6 7-6" fill="none" stroke="#1e88e5" stroke-width="1.6"/></svg>Email address</div>
  <div class="field message" style="top:3398px">Message</div>
  <a class="send-btn">SEND ENQUIRY</a>
  <div class="contact-photo-ring"><div class="contact-photo" role="img" aria-label="Wooden dock on a still lake with autumn trees"></div></div>
</section>

<footer>
  <div class="footer-brand">
    <div class="brand"><span class="brand-dot"></span><span class="brand-name">Brookvane</span></div>
    <p>Brookvane LLC is a company formed in response to the increasing incidence of invasive species in Minnesota's lakes and waters.</p>
    <div class="socials"><span></span><span></span><span></span><span></span></div>
  </div>
  <div class="footer-col" style="left:522px">
    <h4>QUICK LINKS</h4>
    <div class="link-grid"><span>Home</span><span>FAQs</span><span>Services</span><span>Employment</span><span>About Us</span><span>Testimonials</span><span>Contact Us</span><span>Gallery</span></div>
  </div>
  <div class="footer-col" style="left:860px">
    <h4>CONTACT US</h4>
    <ul class="contact-list">
      <li><svg width="14" height="18" viewBox="0 0 14 18"><path d="M7 0a7 7 0 0 1 7 7c0 5-7 11-7 11S0 12 0 7a7 7 0 0 1 7-7Z" fill="#1e88e5"/><circle cx="7" cy="7" r="2.5" fill="#fff"/></svg><span>4120 Birch Trail<br>Alder Bay, MN 55000</span></li>
      <li><svg width="16" height="12" viewBox="0 0 16 12"><rect width="16" height="12" rx="1" fill="#1e88e5"/><path d="M1 1l7 6 7-6" fill="none" stroke="#fff" stroke-width="1.4"/></svg><span>hello@brookvane.com</span></li>
      <li><svg width="16" height="16" viewBox="0 0 16 16"><path d="M3 1l3 3-2 2q2 4 6 6l2-2 3 3-2 2Q5 15 1 3Z" fill="#1e88e5"/></svg><span>(555) 014-2280</span></li>
    </ul>
  </div>
  <div class="copyright">Copyright 2020 Brookvane LLC</div>
</footer>

</body>
</html>
```